Non-governmental organisation branding design

We are looking to get the branding for our new NGO:

Kestrel Harbour Centre

Our tag-line is: Peace through dialogue

We are a peace brokering organisation that conducts research and offers peace brokering services relating to conflicts around the world.

The branding needs to be simple, to the point and serious.

Other comparable organisations are:

https://www.vantrellhub.org/

http://tlx.fi/

https://www.oravelle.org/

Any questions, please get in touch.

Logo Text

Kestrel Harbour Centre

Number of Pages Required

1 page

```html
<!DOCTYPE html>
<html lang="en">
<head>
<meta charset="utf-8">
<title>Kestrel Harbour Centre</title>
<link rel="stylesheet" href="https://fonts.googleapis.com/css2?family=Lato:wght@300;400;700;900&family=Oswald:wght@400&display=swap">
<style>
:root{
  --blue:#2b5ca6;
  --red:#8c1b20;
  --band:#f2f2f2;
  --text:#333;
  --muted:#555;
  --line:#e2e2e2;
  --footer:#222;
  --footer-bottom:#191919;
  --footer-text:#cfcfcf;
}
*{box-sizing:border-box;margin:0;padding:0}
html,body{width:1200px;height:3805px;overflow:hidden;background:#fff}
body{font-family:"Lato",sans-serif;color:var(--text);position:relative}
.wrap{position:absolute;left:76px;width:1048px}
a{color:inherit;text-decoration:none}

/* header */
.site-header{position:absolute;top:0;left:0;width:1200px;height:85px;background:#fff}
.brand{position:absolute;left:76px;top:24px;font-family:"Oswald",sans-serif;font-size:32px;color:var(--blue);letter-spacing:.5px;text-transform:uppercase}
.main-nav{position:absolute;right:76px;top:36px;display:flex;gap:30px;font-size:13px;font-weight:700;text-transform:uppercase;color:#222}
.main-nav .active{color:var(--blue)}

/* hero */
.hero{position:absolute;top:85px;left:0;width:1200px;height:583px;background:linear-gradient(180deg,#4a4b4e 0%,#6b6360 45%,#3d3f44 100%)}
.hero-title{position:absolute;top:250px;width:100%;text-align:center;color:#fff;font-size:56px;font-weight:900;text-shadow:0 2px 6px rgba(0,0,0,.4)}
.hero-dots{position:absolute;top:527px;left:0;width:100%;display:flex;justify-content:center;gap:8px}
.hero-dots span{width:11px;height:11px;border-radius:50%;background:#fff}

/* common */
.section-band{position:absolute;left:0;width:1200px;height:92px;background:var(--band);display:flex;align-items:center;justify-content:center}
.section-title{font-size:34px;font-weight:300;color:var(--blue);text-transform:uppercase;letter-spacing:1px}
.intro{position:absolute;left:0;width:1200px;text-align:center;font-size:14px;color:var(--text)}
.btn{display:inline-block;background:var(--red);color:#fff;font-size:14px;font-weight:700;text-transform:uppercase;text-align:center;line-height:48px;height:48px}

/* welcome */
.welcome-title{position:absolute;top:718px;left:0;width:1200px;text-align:center}
.welcome-text{position:absolute;top:782px;left:76px;width:500px;font-size:14px;line-height:25px;color:var(--muted)}
.welcome .btn{position:absolute;left:76px;top:1025px;width:150px}
.video{position:absolute;left:614px;top:787px;width:511px;height:286px;background:linear-gradient(135deg,#7d7d80,#c9c6c1 55%,#4b4d52)}
.video svg{position:absolute;left:229px;top:116px}

/* cards */
.card{position:absolute;width:330px;border:1px solid var(--line);background:#fff;text-align:center}
.service{top:1318px;height:276px}
.service svg{margin-top:44px}
.card-title{font-size:17px;font-weight:700;color:var(--blue);text-transform:uppercase}
.service .card-title{margin-top:14px}
.card-text{font-size:14px;line-height:21px;color:var(--muted);padding:0 36px;margin-top:8px}
.card .btn{position:absolute;left:89px;bottom:-24px;width:152px}

/* map */
.world-map{position:absolute;left:228px;top:1877px;width:750px;height:356px;border-radius:40px;background:radial-gradient(ellipse at center,#d0d0d0 0%,#e8e8e8 60%,#fff 100%)}

/* team */
.member{position:absolute;top:2463px;width:240px;text-align:center}
.portrait{width:240px;height:203px;background:linear-gradient(180deg,#bfbfbf,#8a8a8a)}
.member .card-title{margin-top:36px;font-size:16px}
.role{font-size:14px;color:var(--red);margin-top:4px}
.member .card-text{padding:0 8px;margin-top:6px;font-size:14px;line-height:20px}
.text-link{display:block;margin-top:12px;font-size:12px;color:var(--red);text-transform:uppercase}

/* blog */
.post{top:3118px;height:277px;padding-top:34px}
.post-date{font-size:14px;font-weight:700;color:var(--red)}
.post .card-title{margin-top:10px;font-size:16px;line-height:24px;padding:0 30px}
.post .card-text{margin-top:10px}

/* footer */
.site-footer{position:absolute;top:3483px;left:0;width:1200px;height:267px;background:var(--footer);color:var(--footer-text)}
.footer-col{position:absolute;top:58px}
.footer-col h4{font-size:16px;font-weight:700;color:#fff;text-transform:uppercase;margin-bottom:14px}
.footer-col ul{list-style:none;font-size:12px;line-height:29px}
.sitemap ul{columns:2;column-gap:40px;width:230px}
.signup p{font-size:12px;line-height:20px;width:210px}
.signup .email{margin-top:16px;width:241px;height:41px;background:#fff;color:#333;font-size:12px;padding:0 14px;line-height:41px}
.signup .submit{position:absolute;left:152px;top:140px;width:89px;height:33px;background:var(--blue);color:#fff;font-size:12px;font-weight:700;text-transform:uppercase;text-align:center;line-height:33px}
.footer-bottom{position:absolute;top:3750px;left:0;width:1200px;height:55px;background:var(--footer-bottom);color:#aaa;font-size:11px}
.footer-bottom .copy{position:absolute;left:76px;top:21px}
.social{position:absolute;right:76px;top:19px;display:flex;gap:16px}
.social span{width:16px;height:16px;border-radius:50%;background:#bbb}
</style>
</head>
<body>

<header class="site-header">
  <div class="brand">Kestrel Harbour Centre</div>
  <nav class="main-nav">
    <a class="active">Home</a><a>About Us</a><a>Services</a><a>Projects</a><a>Blog</a><a>News</a><a>Contact Us</a>
  </nav>
</header>

<section class="hero" role="img" aria-label="Photo of three smiling colleagues joining hands in an office">
  <h1 class="hero-title">Peace Through Dialogue</h1>
  <div class="hero-dots"><span></span><span></span><span></span></div>
</section>

<section class="welcome">
  <h2 class="section-title welcome-title">Welcome to our website</h2>
  <p class="welcome-text">Lorem ipsum dolor sit amet, consectetur adipiscing elit. Quisque pharetra blandit dignissim. Morbi ac imperdiet velit, eget tristique eros. Ut efficitur suscipit nulla. Mauris non elit posuere, vehicula tortor sed, lacinia leo. Aenean euismod vulputate vehicula. Mauris tempor, elit ac condimentum accumsan, ante augue tristique magna, at rhoncus risus mauris id leo. Cras aliquet tellus at dui tempus, non ultrices nulla iaculis. Nulla at finibus lorem. In vestibulum mauris id elit finibus euismod. Vivamus placerat rutrum eros quis feugiat.</p>
  <a class="btn">Read More</a>
  <div class="video" role="img" aria-label="Video still of a business meeting around a laptop">
    <svg width="52" height="52" viewBox="0 0 52 52"><circle cx="26" cy="26" r="25" fill="#fff"/><path d="M21 15 L37 26 L21 37 Z" fill="#333"/></svg>
  </div>
</section>

<div class="section-band" style="top:1137px"><h2 class="section-title">What we do</h2></div>
<p class="intro" style="top:1262px">Lorem ipsum dolor sit amet, consectetur adipiscing elit. Quisque pharetra blandit dignissim. Morbi ac imperdiet velit, eget tristique eros.</p>

<div class="card service" style="left:76px">
  <svg width="76" height="60" viewBox="0 0 76 60" fill="#555"><circle cx="38" cy="16" r="12"/><circle cx="14" cy="22" r="9"/><circle cx="62" cy="22" r="9"/><path d="M18 60 C18 38 58 38 58 60Z"/><path d="M0 56 C0 38 26 36 26 44 L22 56Z"/><path d="M76 56 C76 38 50 36 50 44 L54 56Z"/></svg>
  <h3 class="card-title">Mediation and Dialogue</h3>
  <p class="card-text">Ut efficitur suscipit nulla. Mauris non elit posuere, vehicula tortor sed, lacinia euismod vulputate vehicula.</p>
  <a class="btn">Read More</a>
</div>
<div class="card service" style="left:435px">
  <svg width="76" height="60" viewBox="0 0 76 60" fill="#555"><ellipse cx="32" cy="22" rx="30" ry="20"/><path d="M12 36 L6 52 L26 40Z"/><ellipse cx="52" cy="36" rx="22" ry="15" fill="#fff"/><ellipse cx="52" cy="36" rx="19" ry="12.5"/><path d="M64 46 L72 58 L58 48Z"/></svg>
  <h3 class="card-title">Mediation Support</h3>
  <p class="card-text">Ut efficitur suscipit nulla. Mauris non elit posuere, vehicula tortor sed, lacinia euismod vulputate vehicula.</p>
  <a class="btn">Read More</a>
</div>
<div class="card service" style="left:795px">
  <svg width="76" height="60" viewBox="0 0 76 60"><path d="M22 0 H46 L60 14 V60 H22Z" fill="#555"/><path d="M46 0 V14 H60Z" fill="#999"/><rect x="28" y="24" width="26" height="4" fill="#fff"/><rect x="28" y="33" width="26" height="4" fill="#fff"/><rect x="28" y="42" width="26" height="4" fill="#fff"/></svg>
  <h3 class="card-title">Policy and Learning</h3>
  <p class="card-text">Ut efficitur suscipit nulla. Mauris non elit posuere, vehicula tortor sed, lacinia euismod vulputate vehicula.</p>
  <a class="btn">Read More</a>
</div>

<div class="section-band" style="top:1690px"><h2 class="section-title">Where we work</h2></div>
<p class="intro" style="top:1814px">Lorem ipsum dolor sit amet, consectetur adipiscing elit. Quisque pharetra blandit dignissim. Morbi ac imperdiet velit, eget tristique eros.</p>
<div class="world-map" role="img" aria-label="Dotted world map with red location pins on each continent"></div>

<div class="section-band" style="top:2278px"><h2 class="section-title">Our team</h2></div>
<p class="intro" style="top:2405px">Lorem ipsum dolor sit amet, consectetur adipiscing elit. Quisque pharetra blandit dignissim. Morbi ac imperdiet velit, eget tristique eros.</p>

<div class="member" style="left:76px">
  <div class="portrait" role="img" aria-label="Portrait photo of a team member"></div>
  <h3 class="card-title">Name Heading</h3><p class="role">Director</p>
  <p class="card-text">Lorem ipsum dolor sit amet, consectetur adipiscing elit blandit dignissim ac imperdiet velit, eget tristique eros.</p>
  <a class="text-link">Read More</a>
</div>
<div class="member" style="left:345px">
  <div class="portrait" role="img" aria-label="Portrait photo of a team member"></div>
  <h3 class="card-title">Name Heading</h3><p class="role">Director</p>
  <p class="card-text">Lorem ipsum dolor sit amet, consectetur adipiscing elit blandit dignissim ac imperdiet velit, eget tristique eros.</p>
  <a class="text-link">Read More</a>
</div>
<div class="member" style="left:614px">
  <div class="portrait" role="img" aria-label="Portrait photo of a team member"></div>
  <h3 class="card-title">Name Heading</h3><p class="role">Director</p>
  <p class="card-text">Lorem ipsum dolor sit amet, consectetur adipiscing elit blandit dignissim ac imperdiet velit, eget tristique eros.</p>
  <a class="text-link">Read More</a>
</div>
<div class="member" style="left:884px">
  <div class="portrait" role="img" aria-label="Portrait photo of a team member"></div>
  <h3 class="card-title">Name Heading</h3><p class="role">Director</p>
  <p class="card-text">Lorem ipsum dolor sit amet, consectetur adipiscing elit blandit dignissim ac imperdiet velit, eget tristique eros.</p>
  <a class="text-link">Read More</a>
</div>

<div class="section-band" style="top:2935px"><h2 class="section-title">Blog posts</h2></div>
<p class="intro" style="top:3062px">Lorem ipsum dolor sit amet, consectetur adipiscing elit. Quisque pharetra blandit dignissim. Morbi ac imperdiet velit, eget tristique eros.</p>

<article class="card post" style="left:76px">
  <p class="post-date">JUL 26, 2018</p>
  <h3 class="card-title">Suspendisse non nisl nec suscipit mi eu...</h3>
  <p class="card-text">Ut efficitur suscipit nulla. Mauris non elit posuere, vehicula tortor sed, lacinia euismod vulputate vehicul eleifend augue ut lorem ullamcorper finibus..</p>
  <a class="btn">Read More</a>
</article>
<article class="card post" style="left:435px">
  <p class="post-date">JUL 26, 2018</p>
  <h3 class="card-title">Suspendisse non nisl nec suscipit mi eu...</h3>
  <p class="card-text">Ut efficitur suscipit nulla. Mauris non elit posuere, vehicula tortor sed, lacinia euismod vulputate vehicul eleifend augue ut lorem ullamcorper finibus..</p>
  <a class="btn">Read More</a>
</article>
<article class="card post" style="left:795px">
  <p class="post-date">JUL 26, 2018</p>
  <h3 class="card-title">Suspendisse non nisl nec suscipit mi eu...</h3>
  <p class="card-text">Ut efficitur suscipit nulla. Mauris non elit posuere, vehicula tortor sed, lacinia euismod vulputate vehicul eleifend augue ut lorem ullamcorper finibus..</p>
  <a class="btn">Read More</a>
</article>

<footer class="site-footer">
  <div class="footer-col sitemap" style="left:76px">
    <h4>Site Map</h4>
    <ul><li>Home</li><li>About Us</li><li>Services</li><li>Projects</li><li>Blog</li><li>News</li><li>Contact Us</li></ul>
  </div>
  <div class="footer-col" style="left:383px">
    <h4>Services</h4>
    <ul><li>Nulla at finibus lorem</li><li>Vestibulum</li><li>Elit finibus</li><li>Euismod</li></ul>
  </div>
  <div class="footer-col" style="left:632px">
    <h4>Resources</h4>
    <ul><li>Nulla at finibus lorem</li><li>Vestibulum</li><li>Elit finibus</li><li>Euismod</li></ul>
  </div>
  <div class="footer-col signup" style="left:883px">
    <h4>Email Sign Up</h4>
    <p>Nulla at finibus lorem vestibulum elit finibus euismod.</p>
    <div class="email">Enter Email Address</div>
    <div class="submit">Sign Up</div>
  </div>
</footer>
<div class="footer-bottom">
  <p class="copy">Copyright © 2018. Company Name All Right Reserved</p>
  <div class="social"><span></span><span></span><span></span><span></span><span></span><span></span></div>
</div>

</body>
</html>
```